I need a proposal brochure designed

I need a brochure designed to give to a company as a proposal to win a corporate health and fitness contract. I have an existing brochure design that I really like so I would like to see designs using this existing brochure as a template. I want it to be easy to read and visually appealing.

```html
<!DOCTYPE html>
<html lang="en">
<head>
<meta charset="utf-8">
<title>Peak Stride – Corporate Fitness Proposal</title>
<link rel="stylesheet" href="https://fonts.googleapis.com/css2?family=Montserrat:wght@300;400;500;600;700;800&display=swap">
<style>
:root{
  --blue:#1c4eae;
  --blue-dark:#163f91;
  --yellow:#fddc2e;
  --ink:#2b2b2b;
  --muted:#6b6b6b;
  --canvas:#e4e4e4;
  --label:#9c9c9c;
}
*{box-sizing:border-box;margin:0;padding:0}
html,body{width:1200px;height:3599px;overflow:hidden}
body{background:linear-gradient(180deg,#e9e9e9,#dedede);font-family:'Montserrat',sans-serif;color:var(--ink);position:relative}
.page-label{position:absolute;font-size:28px;font-weight:400;color:var(--label);letter-spacing:1px}
.sheet{position:absolute;left:223px;width:758px;height:535px;background:#fff;box-shadow:2px 3px 6px rgba(0,0,0,.28);overflow:hidden}
.shapes{position:absolute;left:0;top:0}
.pg{position:absolute;top:0;width:379px;height:535px}
.pg.r{left:379px}
.title{position:absolute;top:0;left:0;width:379px;height:95px;display:flex;align-items:center;justify-content:center;text-align:center;font-weight:700;font-size:17px;letter-spacing:3px;line-height:1.15}
.t-white{color:#fff}.t-blue{color:var(--blue)}.t-yellow{color:var(--yellow)}
.copy p{font-size:6.2px;line-height:1.5;margin-bottom:5px;color:var(--ink)}
.copy.white p{color:#fff}
.hd{font-size:8.5px;font-weight:700;color:var(--blue);text-align:center;letter-spacing:.3px}
.hd-l{font-size:8px;font-weight:700;color:var(--blue);letter-spacing:.5px}
ul.list{list-style:none}
ul.list li{position:relative;padding-left:11px;font-size:6px;line-height:1.45;margin-bottom:5px}
ul.list li::before{content:"";position:absolute;left:0;top:2px;width:5px;height:5px;background:var(--yellow);transform:skewX(-12deg)}
ul.list.bl li::before{background:var(--blue)}
.b{font-weight:700;color:var(--blue)}
.abs{position:absolute}
.tagline{font-size:17px;line-height:1.3;color:#fff;font-weight:400}
.tagline strong{font-weight:700;font-size:24px}
.contact{font-size:6.5px;line-height:2;color:#fff;font-weight:600}
table.price{width:100%;border-collapse:collapse;font-size:5.6px;text-align:center}
table.price th{color:var(--blue);font-weight:700;border-bottom:1.5px solid var(--blue);padding:2px}
table.price td{padding:3px 2px;border-right:1px solid #bbb;vertical-align:top;line-height:1.4}
table.price td:last-child{border-right:none}
.note{font-size:5.4px;text-align:center;color:var(--muted);line-height:1.4}
.badge{position:absolute;width:92px;height:92px;border-radius:50%;display:flex;align-items:center;justify-content:center;text-align:center;font-size:5.6px;line-height:1.4;padding:12px}
.badge.y{background:var(--yellow);color:var(--blue)}
.badge.bl{background:var(--blue);color:#fff}
.badge.w{background:#fff;color:var(--ink)}
.star{position:absolute;width:14px;height:14px}
.partner{position:absolute;height:12px;border-radius:3px;background:#c9c9c9}
.field{position:absolute;font-size:6px;color:var(--ink);width:150px;border-bottom:1px dotted #888;padding-bottom:1px}
</style>
</head>
<body>

<div class="page-label" style="left:11px;top:553px">BACK PAGE</div>
<div class="page-label" style="left:1000px;top:553px">FRONT</div>
<div class="page-label" style="left:95px;top:1127px">P2</div>
<div class="page-label" style="left:1069px;top:1127px">P3</div>
<div class="page-label" style="left:95px;top:1708px">P4</div>
<div class="page-label" style="left:1069px;top:1708px">P5</div>
<div class="page-label" style="left:95px;top:2289px">P6</div>
<div class="page-label" style="left:1069px;top:2289px">P7</div>
<div class="page-label" style="left:95px;top:2870px">P8</div>
<div class="page-label" style="left:1069px;top:2870px">P9</div>
<div class="page-label" style="left:95px;top:3478px">P10</div>
<div class="page-label" style="left:1055px;top:3478px">P11</div>

<!-- Spread 1: Cover -->
<section class="sheet cover" style="top:57px;background:var(--blue)">
  <svg class="shapes" width="758" height="535" aria-hidden="true">
    <line x1="379" y1="0" x2="379" y2="535" stroke="var(--blue-dark)" stroke-width="1"/>
    <polygon points="421,22 658,22 723,87 723,265 421,265" fill="var(--yellow)"/>
  </svg>
  <div class="pg back">
    <div class="abs" style="left:22px;top:353px;width:92px;height:92px;border-radius:50%;background:var(--yellow)"></div>
    <div class="abs tagline" style="left:24px;top:458px;font-size:13px">Your Life<br>Your Potential<br><strong style="font-size:18px">Your Stride</strong></div>
    <div class="abs contact" style="left:221px;top:458px">www.peakstride.example<br>✉ reid@peakstride.example<br>◎ @peakstridecoach<br>◉ @ourpeakstride</div>
  </div>
  <div class="pg r front">
    <div class="abs" style="left:42px;top:228px;width:302px;text-align:center;font-size:16px;color:var(--blue);font-weight:500;letter-spacing:.5px">PEAK STRIDE</div>
    <div class="abs tagline" style="left:38px;top:348px">Your Life<br>Your Potential<br><strong>Your Stride</strong></div>
    <div class="abs" style="left:38px;top:452px;color:#fff;font-size:13px">Fitness and Wellness</div>
    <div class="abs" style="left:38px;top:468px;color:#fff;font-size:6.5px;line-height:1.55">Implementing Corporate Fitness Services<br>PREPARED FOR:&nbsp;&nbsp;&nbsp;&nbsp;&nbsp;&nbsp;&nbsp;&nbsp;<b>BRIGHTFIELD GROUP</b><br>PREPARED BY:&nbsp;&nbsp;&nbsp;&nbsp;&nbsp;&nbsp;&nbsp;&nbsp;&nbsp;&nbsp;<b>PEAK STRIDE</b><br><span style="padding-left:70px">(Fitness &amp; Lifestyle Coaching)</span></div>
  </div>
</section>

<!-- Spread 2 -->
<section class="sheet" style="top:638px">
  <svg class="shapes" width="758" height="535" aria-hidden="true">
    <polygon points="0,0 379,0 379,260 270,95 0,95" fill="var(--yellow)"/>
    <rect x="379" y="0" width="379" height="95" fill="var(--blue)"/>
    <rect x="379" y="95" width="379" height="161" fill="var(--yellow)"/>
  </svg>
  <div class="pg">
    <div class="abs copy" style="left:22px;top:116px;width:215px">
      <p>Dear Marco, Elena, Paolo and the rest of the Lamberti family,</p>
      <p>I am excited to present you with a comprehensive proposal for providing personal training and fitness services to <span class="b">Brightfield Group</span>. I am committed to delivering exceptional fitness results by optimizing the performance and overall well-being of your family and your employees at all levels. I have crafted this proposal to offer my expertise through standalone personal training sessions as well as ongoing corporate wellness programs.</p>
      <p>The proposal outlines the current situation, needs, outcomes and hopes as I have understood it from our previous discussions.</p>
      <p>While the proposal is designed to meet your criteria for hiring an experienced personal trainer to provide sales fitness and wellness services, it's not exhaustive. Health and wellness, more so than any other area in life, requires ongoing commitment and attention to continuously maximize results.</p>
      <p>So this proposal is designed to meet immediate to short term needs, with a view to an on-going relationship in the future, should both of us see the outcomes we are hoping for.</p>
      <p>If you have any questions or would like to adjust the scope of the proposal, please don't hesitate to reach out.</p>
      <p>Sincerely,</p>
      <p style="margin-top:12px">Reid Calloway<br>Founder &amp; Owner</p>
      <p><span class="b">Peak Stride</span><br>Fitness and Lifestyle Coaching</p>
    </div>
  </div>
  <div class="pg r">
    <div class="title t-white">PROJECT SUMMARY</div>
    <div class="abs copy white" style="left:56px;top:114px;width:282px">
      <p><b style="color:var(--blue)">Brightfield Group</b> wants to equip their employees with the knowledge and skills they need to take care of their own health and wellbeing.</p>
      <p>Not all employees are prioritizing their health and wellness which impacts their ability to perform at their highest level within the company and reduces their quality of life in and outside work.</p>
      <p>The Lamberti family would like to ensure that each of their family members have access to their own personal training sessions so that they can each improve their fitness and performance, and to achieve their own individual health and wellness goals.</p>
    </div>
    <div class="abs" style="left:148px;top:272px;width:84px;text-align:center">
      <div style="width:22px;height:22px;border-radius:50%;background:#c9b98a;margin:0 auto 4px"></div>
      <div style="font-size:9px;letter-spacing:3px;color:#9a8a5e">BRIGHTFIELD</div>
    </div>
    <div class="abs hd" style="left:0;top:330px;width:379px">THE PROJECT OUTCOMES ARE AS FOLLOWS</div>
    <ul class="abs list" style="left:56px;top:350px;width:282px">
      <li>Have each family member committed to personal training sessions on a weekly basis.</li>
      <li>Develop quarterly goals and annual goals for each family member specific to their individual needs.</li>
      <li>Implement positive lifestyle changes that will improve quality of life and lifespan.</li>
      <li>Show <span class="b">Brightfield Group</span> employees that, as a company, Brightfield Group cares about their quality of life not only at work but outside of it as well.</li>
      <li>Create a culture that embodies health and wellness as a tool to create high performance and reduce burn out.</li>
      <li>Develop an annual corporate fitness and wellness program that is easily accessible for all employees.</li>
    </ul>
  </div>
</section>

<!-- Spread 3 -->
<section class="sheet" style="top:1219px">
  <svg class="shapes" width="758" height="535" aria-hidden="true">
    <rect x="379" y="0" width="379" height="95" fill="var(--yellow)"/>
    <polygon points="0,0 475,0 379,95 0,95" fill="var(--blue)"/>
    <rect x="0" y="424" width="379" height="111" fill="var(--yellow)"/>
  </svg>
  <div class="pg">
    <div class="title t-white">PROJECT DETAILS</div>
    <div class="abs hd-l" style="left:25px;top:120px">CURRENT SITUATION</div>
    <ul class="abs list" style="left:25px;top:136px;width:120px">
      <li>Not all family members are prioritizing their fitness and health.</li>
      <li>There is untapped potential to improve productivity and results. Fit and healthy people can push themselves to work hard and be more efficient.</li>
      <li>High performance creates high stress, high stress creates burn out and reduces quality of life.</li>
      <li>There is a buildup of chronic injuries from lack of fitness and movement that need to be addressed.</li>
      <li>There are no current health and wellness initiatives at Brightfield Group.</li>
      <li>Employees who aren't taking care of themselves physically and mentally use more sick days and aren't performing at their optimal abilities.</li>
    </ul>
    <div class="abs hd-l" style="left:170px;top:120px">GOALS &amp; REQUIREMENTS</div>
    <ul class="abs list bl" style="left:170px;top:136px;width:190px">
      <li>Have access to 'at home' professional personal training services at times that suit each individual family member's schedule.</li>
      <li>To have the ability to change personal training time slots when weekly calendars change to ensure sessions are never missed.</li>
      <li>Having someone personally invested in the success of each family member as individuals and as a whole family unit.</li>
      <li>Create individual plans to achieve quarterly and annual fitness goals, be it weight loss, reduce injuries, gain muscle or improve lifespan and overall well being.</li>
      <li>Engage with Brightfield Group employees to set up a Health and Wellness club to help them achieve their own personal fitness goals.</li>
      <li>Create monthly health and wellness presentations for Brightfield Group employees to participate in.</li>
      <li>Provide virtual or in office fitness classes for Brightfield Group employees.</li>
    </ul>
    <div class="abs" role="img" aria-label="Raised fist emblem" style="left:22px;top:448px;width:62px;height:62px;border-radius:50%;border:1.5px solid var(--blue)"></div>
    <div class="abs hd" style="left:100px;top:447px;width:260px">ULTIMATE RESULT</div>
    <div class="abs copy" style="left:102px;top:462px;width:258px"><p>Provide bespoke, world class fitness training and lifestyle optimization coaching for each Lamberti family member to help improve their lives as individuals and as a family. Create a health and wellness corporate program for Brightfield Group which will add value to their life at work and in their personal lives.</p></div>
  </div>
  <div class="pg r">
    <div class="title t-blue">MY PROCESS</div>
    <div class="abs hd" style="left:0;top:120px;width:379px">1. PEAK STRIDE METHODOLOGY</div>
    <div class="abs copy" style="left:22px;top:134px;width:340px"><p>In order to take control of your health and fitness you need to go through these 5 steps:</p></div>
    <svg class="abs" style="left:28px;top:150px" width="26" height="200" aria-hidden="true" fill="none" stroke="var(--blue)" stroke-width="1.3">
      <ellipse cx="13" cy="12" rx="10" ry="6"/><circle cx="13" cy="12" r="3"/>
      <rect x="3" y="50" width="18" height="10" rx="5"/><line x1="12" y1="60" x2="24" y2="60"/>
      <rect x="5" y="90" width="15" height="19" rx="1"/><line x1="8" y1="96" x2="17" y2="96"/><line x1="8" y1="101" x2="17" y2="101"/>
      <circle cx="13" cy="140" r="8"/><line x1="9" y1="140" x2="17" y2="140"/>
      <polyline points="4,172 16,172 8,182 20,182"/><polyline points="15,177 20,182 15,187"/>
    </svg>
    <div class="abs copy" style="left:66px;top:152px;width:296px">
      <p><span class="b">Clarity:</span> Figure out your Who, What, Why, How to gain a deeper understanding of yourself and discover your short and long term goals.</p>
      <p style="margin-top:10px"><span class="b">Measurement:</span> When you track it you can improve it. Discover the metrics required to track to determine how you are improving and the results you are achieving.</p>
      <p style="margin-top:8px"><span class="b">Discipline:</span> Create positive habits and maintain them through strict routines. These keep you accountable to yourself and the bigger picture, which is to live a balanced, high performing life in all aspects.</p>
      <p style="margin-top:6px"><span class="b">Nutrition:</span> Eat healthy, Live well, Feel great. Only when we fill our body with not only the right ingredients, but the right amount can we achieve the physical and mental states we desire.</p>
      <p style="margin-top:6px"><span class="b">Exercise:</span> Movement is the foundation of life. To run on all cylinders and remain injury free, we need to be exerting ourselves physically through working out and different movement patterns.</p>
    </div>
    <div class="abs hd" style="left:0;top:372px;width:379px">2. PERSONAL TRAINING</div>
    <div class="abs copy" style="left:22px;top:388px;width:340px">
      <p>What are your goals? What sort of exercise do you like, dislike? Do you have any injuries? What are your eating habits like? What will it take to make working out a priority for the rest of your life?</p>
      <p>These are all fundamental questions that I like to ask in order to be an effective personal trainer. The foundation of living a life maximized to its true potential is figuring out a lifestyle and plan that allows you to be disciplined enough to achieve your fitness goals without compromising your enjoyment of the finer things in life, like a big piece of cake at a birthday celebration.</p>
      <p>Unlike most personal trainers who have created one plan that every client goes through, I create unique plans for each individual, based on their own unique goals and priorities in life. Spending the time to deeply understand each individual's goals and struggles, I can then create solutions to accelerate improved fitness and overall wellbeing.</p>
    </div>
  </div>
</section>

<!-- Spread 4 -->
<section class="sheet" style="top:1800px;left:219px">
  <svg class="shapes" width="758" height="535" aria-hidden="true">
    <rect x="0" y="0" width="379" height="95" fill="var(--yellow)"/>
    <polygon points="284,0 758,0 758,95 379,95" fill="var(--blue)"/>
  </svg>
  <div class="pg">
    <div class="title t-blue" style="width:290px">THE FORMAT</div>
    <div class="abs" style="left:0;top:118px;width:379px;text-align:center;color:var(--blue);font-weight:800;font-size:15px">PHASE 1</div>
    <div class="abs hd" style="left:0;top:136px;width:379px">PERSONAL TRAINING FOR EACH LAMBERTI FAMILY MEMBER</div>
    <svg class="abs" style="left:36px;top:160px" width="22" height="92" aria-hidden="true" fill="none" stroke="var(--blue)" stroke-width="1.3">
      <circle cx="11" cy="10" r="8"/><line x1="11" y1="6" x2="11" y2="14"/>
      <rect x="2" y="38" width="16" height="9" rx="4.5"/><line x1="10" y1="47" x2="21" y2="47"/>
      <polyline points="3,70 15,70 7,80 19,80"/><polyline points="14,75 19,80 14,85"/>
    </svg>
    <div class="abs" style="left:70px;top:160px;width:290px">
      <div class="hd-l" style="font-size:7.5px;letter-spacing:1px">GATHER INFORMATION</div>
      <div style="font-size:6px;line-height:1.4">1:1 consultation to understand short term/long term goals (revisited when needed)</div>
      <div class="hd-l" style="font-size:7.5px;letter-spacing:1px;margin-top:8px">TAKE MEASUREMENTS</div>
      <div style="font-size:6px;line-height:1.4">Record relevant data points based off individual goals to track results, body fat %, weight etc</div>
      <div class="hd-l" style="font-size:7.5px;letter-spacing:1px;margin-top:8px">THE TRAINING</div>
      <div style="font-size:6px;line-height:1.4">1:1 'in house' personal training sessions focused on implementation of fitness plan</div>
    </div>
    <div class="abs" style="left:0;top:280px;width:379px;text-align:center;color:var(--blue);font-weight:800;font-size:15px">PHASE 2</div>
    <div class="abs hd" style="left:0;top:298px;width:379px;line-height:1.25">CORPORATE HEALTH &amp; WELLNESS PROGRAM<br>FOR BRIGHTFIELD GROUP</div>
    <ul class="abs list" style="left:22px;top:330px;width:340px">
      <li>Monthly in person 'Health and Wellness' Lunch and Learn discussions (different topics)<br>12 x 45 mins sessions</li>
      <li>Implement 'Health and Wellness Club' for employees. Participants form small accountability groups to help encourage each other to work towards a specific health goal. Run quarterly with prizes and giveaways.<br>4 x 45 min sessions</li>
      <li>20 mins Quarterly virtual 'Check in' call for each group participating</li>
      <li>Weekly lunchtime fitness class at office, all levels</li>
      <li>40 min class per week</li>
      <li>Weekly virtual fitness classes for all levels of fitness, inclusive for all employees to be able to participate</li>
      <li>3 x 45 min virtual classes per week Mon / Wed / Fri 6.30am – 7.15am</li>
    </ul>
  </div>
  <div class="pg r">
    <div class="title t-yellow">WHO AM I</div>
    <div class="abs" role="img" aria-label="Photo of the coach crouching on an outdoor sports field" style="left:0;top:95px;width:146px;height:440px;background:linear-gradient(180deg,#c7cdd3 0%,#9aa3ab 45%,#5e6b5a 80%,#4b5a44 100%)"></div>
    <div class="abs" style="left:53px;top:447px;width:48px;height:48px;border-radius:50%;background:var(--blue)"></div>
    <div class="abs copy" style="left:169px;top:122px;width:180px">
      <p><span class="b">Reid Calloway – Toronto</span><br>Founder, <span class="b">Peak Stride</span> (Fitness and Lifestyle Coaching)</p>
      <p>I've always been involved in fitness and sports for as long as I can remember. I grew up in Australia playing tennis, cricket, rugby, skateboarding and surfing to name a few. The defining moment which led me towards a career in fitness was the day I joined a gym at the age of 17.</p>
      <p>From that day on, I started reading fitness magazines, researching workout routines, trying different classes, buying new protein powders. I was hooked!</p>
      <p>Fast forward 20+ years later and here I am living in Toronto, Canada.</p>
      <p>I moved here in 2008 with a suitcase of clothes, no money and big dreams to create a life of purpose and meaning. I started working my way up the corporate gym ladder, from Head Personal Trainer, Group Fitness Manager, to eventually Functional Training Program Director.</p>
      <p>After achieving what I wanted at the corporate level I decided to go out on my own to start two different companies, a personal training business and a cross fitness studio which became one of the city's longest running bootcamps.</p>
      <p>As the saying goes, 'A rolling stone gathers no moss', so eventually it became obvious to me that I needed to combine all of the experience I had gained to create a new and unique approach to executive fitness and lifestyle coaching, and so Peak Stride was born.</p>
    </div>
  </div>
</section>

<!-- Spread 5 -->
<section class="sheet" style="top:2381px">
  <svg class="shapes" width="758" height="535" aria-hidden="true">
    <rect x="0" y="0" width="379" height="95" fill="var(--blue)"/>
    <polygon points="379,0 758,0 758,95 320,95" fill="var(--yellow)"/>
  </svg>
  <div class="pg">
    <div class="title t-white" style="width:330px">YOUR INVESTMENT</div>
    <div class="abs hd" style="left:0;top:113px;width:379px">PERSONAL TRAINING</div>
    <div class="abs" style="left:22px;top:128px;width:335px">
      <table class="price">
        <tr><th>Description</th><th>Time Allocated</th><th>Time Availability</th><th>Total Investment Monthly (CAD)</th></tr>
        <tr><td>1:1 Personal Training for 8 family members<br>2 x week</td><td>40 weeks<br>16 hours of sessions<br>14 hours driving (approx)<br>Elmridge, Harbourview</td><td>Monday–Thurs<br>6am – 7pm<br>Friday<br>6am – 12pm</td><td>$9200<br>(tax included)</td></tr>
      </table>
      <div class="note" style="margin-top:4px">Add Ons: Anyone who wants to do 3 sessions a week add <s>$575</s> $400 per month.</div>
    </div>
    <div class="abs hd" style="left:0;top:230px;width:379px">CORPORATE HEALTH &amp; WELLNESS</div>
    <div class="abs" style="left:22px;top:245px;width:335px">
      <table class="price">
        <tr><th>Description</th><th>Fees</th><th>Packages</th><th>Total Investment Monthly (CAD)</th></tr>
        <tr><td>Lunch and Learn Talks<br>Health &amp; Wellness Club<br>40 min Lunch Classes<br>Virtual Classes<br><br>Copy of Stride Forward for employees</td><td>$500<br>$300<br>$150<br>$10 per person (min/max $200 per class)<br>100 books <s>$2900</s><br>FREE</td><td>12 lunch sessions<br>4 lunch sessions + phone calls (quarterly)<br>48 weeks of workouts Mon/Wed/Fri 6.30am – 7.15am<br>(minus public holidays)</td><td>$3500<br>(tax included)</td></tr>
      </table>
      <div class="note" style="margin-top:4px">Notes: 6 weeks of unpaid vacation have been built into both services for Reid.<br>There is flexibility to make up sessions to ensure sessions aren't missed.</div>
    </div>
    <div class="abs hd" style="left:0;top:382px;width:379px">TOTAL PACKAGE</div>
    <div class="abs" style="left:22px;top:400px;width:335px">
      <table class="price">
        <tr><th>Description</th><th>Total Investment Monthly (CAD)</th></tr>
        <tr><td>Personal Training + Corporate Health &amp; Wellness</td><td>$12700 (includes tax)</td></tr>
      </table>
    </div>
    <div class="abs" style="left:152px;top:460px;width:46px;height:46px;border-radius:50%;background:var(--yellow)"></div>
    <div class="abs" style="left:206px;top:476px;font-size:9px;font-weight:700;color:var(--blue);letter-spacing:1px">PEAK STRIDE</div>
  </div>
  <div class="pg r">
    <div class="title t-blue" style="font-size:17px">ABOUT<br>PEAK STRIDE</div>
    <svg class="star" style="left:64px;top:108px" viewBox="0 0 10 10" aria-hidden="true"><polygon points="5,0 6.2,3.6 10,3.6 7,5.9 8.1,9.5 5,7.3 1.9,9.5 3,5.9 0,3.6 3.8,3.6" fill="var(--blue)"/></svg>
    <svg class="star" style="left:178px;top:108px" viewBox="0 0 10 10" aria-hidden="true"><polygon points="5,0 6.2,3.6 10,3.6 7,5.9 8.1,9.5 5,7.3 1.9,9.5 3,5.9 0,3.6 3.8,3.6" fill="var(--yellow)"/></svg>
    <svg class="star" style="left:291px;top:108px" viewBox="0 0 10 10" aria-hidden="true"><polygon points="5,0 6.2,3.6 10,3.6 7,5.9 8.1,9.5 5,7.3 1.9,9.5 3,5.9 0,3.6 3.8,3.6" fill="var(--blue)"/></svg>
    <svg class="star" style="left:64px;top:231px" viewBox="0 0 10 10" aria-hidden="true"><polygon points="5,0 6.2,3.6 10,3.6 7,5.9 8.1,9.5 5,7.3 1.9,9.5 3,5.9 0,3.6 3.8,3.6" fill="var(--yellow)"/></svg>
    <svg class="star" style="left:178px;top:231px" viewBox="0 0 10 10" aria-hidden="true"><polygon points="5,0 6.2,3.6 10,3.6 7,5.9 8.1,9.5 5,7.3 1.9,9.5 3,5.9 0,3.6 3.8,3.6" fill="var(--blue)"/></svg>
    <svg class="star" style="left:291px;top:231px" viewBox="0 0 10 10" aria-hidden="true"><polygon points="5,0 6.2,3.6 10,3.6 7,5.9 8.1,9.5 5,7.3 1.9,9.5 3,5.9 0,3.6 3.8,3.6" fill="var(--yellow)"/></svg>
    <svg class="star" style="left:64px;top:329px" viewBox="0 0 10 10" aria-hidden="true"><polygon points="5,0 6.2,3.6 10,3.6 7,5.9 8.1,9.5 5,7.3 1.9,9.5 3,5.9 0,3.6 3.8,3.6" fill="var(--blue)"/></svg>
    <svg class="star" style="left:178px;top:329px" viewBox="0 0 10 10" aria-hidden="true"><polygon points="5,0 6.2,3.6 10,3.6 7,5.9 8.1,9.5 5,7.3 1.9,9.5 3,5.9 0,3.6 3.8,3.6" fill="var(--yellow)"/></svg>
    <div class="badge y" style="left:25px;top:115px"><span>Internationally educated with <b>multiple qualifications</b> from Australia and Canada</span></div>
    <div class="badge bl" style="left:139px;top:115px"><span><b>Over 15 years experience</b>, working directly with 100's of clients and facilitated well over 1000 fitness classes</span></div>
    <div class="badge y" style="left:252px;top:115px"><span>We work with executive clients from companies like <b>Norvale, Kestrel Media, Aerlo, Pipfruit</b></span></div>
    <div class="badge bl" style="left:25px;top:238px"><span>In 2014 won <b>'Best Personal Trainer'</b> and 'Best Fitness Program' in Eastern Canada for the Trailhead Monthly Awards</span></div>
    <div class="badge y" style="left:139px;top:238px"><span><b>SELECTED</b> in 2015 to represent Toronto as an Elite Trainer to provide coaching services for Summit Trainer's Global Elite Trainer Network</span></div>
    <div class="badge bl" style="left:252px;top:238px"><span><b>#1 BEST SELLER</b><br>Stride Forward – 5 Steps to Taking Back Control of your Health and Fitness</span></div>
    <div class="badge y" style="left:25px;top:336px"><span><b>FEATURED</b> on UrbanPost, City Wire, Trailhead Monthly</span></div>
    <div class="badge bl" style="left:139px;top:336px"><span>We are best known for helping overworked executives restore life balance through <b>health and fitness</b> optimization while maintaining their career.</span></div>
    <div class="badge w" style="left:252px;top:336px;font-size:6.3px"><span>Learn about<br><b style="color:var(--blue)">Peak Stride</b><br>at<br><b style="color:var(--blue)">www.peakstride.example</b></span></div>
    <div class="partner" style="left:22px;top:462px;width:22px"></div>
    <div class="partner" style="left:56px;top:462px;width:40px"></div>
    <div class="partner" style="left:106px;top:462px;width:24px"></div>
    <div class="partner" style="left:140px;top:462px;width:52px"></div>
    <div class="partner" style="left:204px;top:462px;width:24px"></div>
    <div class="partner" style="left:240px;top:462px;width:100px"></div>
    <div class="partner" style="left:22px;top:494px;width:36px"></div>
    <div class="partner" style="left:68px;top:494px;width:40px"></div>
    <div class="partner" style="left:118px;top:494px;width:30px"></div>
    <div class="partner" style="left:158px;top:494px;width:38px"></div>
    <div class="partner" style="left:206px;top:494px;width:36px"></div>
    <div class="partner" style="left:252px;top:494px;width:22px"></div>
    <div class="partner" style="left:284px;top:494px;width:58px"></div>
  </div>
</section>

<!-- Spread 6 -->
<section class="sheet" style="top:2989px">
  <svg class="shapes" width="758" height="535" aria-hidden="true">
    <rect x="0" y="0" width="480" height="95" fill="var(--yellow)"/>
    <polygon points="480,0 758,0 758,95 379,95" fill="var(--blue)"/>
  </svg>
  <div class="pg">
    <div class="title t-blue">TERMS &amp; CONDITIONS</div>
    <div class="abs hd" style="left:0;top:121px;width:379px">WHAT I PROVIDE</div>
    <ul class="abs list" style="left:76px;top:138px;width:270px">
      <li>Priority access to time slots within my schedule for training</li>
      <li>Flexibility to change time slot when needed</li>
      <li>Unique programs for each individual based of their goals</li>
      <li>Confidentiality (High Priority)</li>
      <li>Punctual for every appointment (High Priority)</li>
      <li>Zero cancellations</li>
      <li>Keep preferred time slots 'blocked' for each individual when needed</li>
      <li>Provide all printed materials and relevant information for Corporate Health and Wellness Club programs</li>
      <li>Availability Mon – Thurs 6am – 7pm Friday 6am–12pm Sat/Sun N/A</li>
    </ul>
    <div class="abs hd" style="left:0;top:300px;width:379px">WHAT YOU PROVIDE</div>
    <ul class="abs list bl" style="left:76px;top:317px;width:270px">
      <li>Commitment to prioritize your health and fitness</li>
      <li>Respect to being on time for personal training sessions</li>
      <li>Notification of canceled sessions</li>
      <li>Follow recommendations and advice given that aligns with your personal goals to the best of your ability.</li>
      <li>Ask for help when needed (No question is a stupid question)</li>
    </ul>
    <div class="abs" style="left:34px;top:440px;font-size:30px;font-weight:800;color:var(--blue);line-height:1">“</div>
    <div class="abs" style="left:68px;top:444px;width:200px;font-size:6px;line-height:1.45">"In this modern world, most people struggle finding the balance between maintaining a high functional career and their body's health and fitness at the same time. Often by the time they realize this, it's too late, the damage of a neglected self has been done."<br><span style="display:block;text-align:right;font-weight:700;color:var(--blue)">– Reid Calloway</span></div>
    <div class="abs" style="left:276px;top:432px;width:70px;height:70px;border-radius:50%;background:var(--blue)"></div>
  </div>
  <div class="pg r">
    <div class="title t-white" style="left:40px;width:339px">TERMS &amp; CONDITIONS</div>
    <div class="abs hd" style="left:0;top:121px;width:379px">CANCELLATIONS &amp; MODIFICATION</div>
    <div class="abs copy" style="left:64px;top:138px;width:260px">
      <p>Any cancellations or modifications made within 24 hours of session will be accommodated to the best of my abilities to suit individuals' schedules, unless conflicting with another Lamberti family member timeslot.</p>
      <p>Any cancellations or modifications made within 24 hours of session will be accommodated to the best of my abilities unless conflicting with my schedule.</p>
      <p>Any cancellations or modifications made within 6 hours of session will be accommodated to the best of my abilities but will have no expectation that session must be made up.</p>
    </div>
    <div class="field" style="left:39px;top:346px">Name</div>
    <div class="field" style="left:205px;top:346px">Name</div>
    <div class="field" style="left:39px;top:376px">Company</div>
    <div class="field" style="left:205px;top:376px">Company</div>
    <div class="field" style="left:39px;top:406px">Position</div>
    <div class="field" style="left:205px;top:406px">Position</div>
    <div class="field" style="left:39px;top:436px">Signature</div>
    <div class="field" style="left:205px;top:436px">Signature</div>
  </div>
</section>

</body>
</html>
```